Meadow Hollow Beauty brand redesign of product labels

national rebrand of skincare product labels - same design but 6 sizes. Will be used for facial serums, body oils, bath salts, room sprays, etc. All labels to be same design - just adjusted for the different sizes. See brand document and sample label.

Bottle Specifications are located in the branding file.
Fonts included in product branding document.
Colours included in branding document.

Featuring company name and logo, product name, product feature, ingredients, size, directions, tag line. See attached sample label as example for design.

Black label base - matt.

Target Market(s)

Natural beauty, 20-60

Industry/Entity Type

farming, natural beauty

Font styles to use
Sans Serif

Requirements
Must have
• Modern, clean, homey
Nice to have
• modern clean design - using the branding colours provided
Should not have
• busy, crowded,

```html
<!DOCTYPE html>
<html lang="en">
<head>
<meta charset="UTF-8">
<title>Meadow Hollow Beauty – Facial Serum Label</title>
<link href="https://fonts.googleapis.com/css2?family=Montserrat:wght@400;600;700&display=swap" rel="stylesheet">
<style>
  :root {
    --canvas: #ffffff;
    --label-base: #2d2e30;
    --label-edge: #1f2021;
    --sage: #a7d28c;
    --teal-line: #5f8a84;
    --text-light: #e4e4e4;
    --text-muted: #a9a9a9;
  }
  * { margin: 0; padding: 0; box-sizing: border-box; }
  html, body {
    width: 1200px;
    height: 1152px;
    overflow: hidden;
    background: var(--canvas);
  }
  .canvas {
    position: relative;
    width: 1200px;
    height: 1152px;
  }
  .label {
    position: absolute;
    left: 280px;
    top: 96px;
    width: 640px;
    height: 960px;
    background: linear-gradient(90deg, var(--label-edge) 0%, var(--label-base) 18%, var(--label-base) 82%, var(--label-edge) 100%);
    font-family: "Montserrat", sans-serif;
    overflow: hidden;
  }
  .brand {
    position: absolute;
    left: 70px;
    top: 110px;
    display: flex;
    align-items: center;
    gap: 14px;
  }
  .brand-mark {
    width: 22px;
    height: 22px;
    border-radius: 50%;
    border: 2px solid var(--teal-line);
    flex: none;
  }
  .brand-name {
    color: var(--sage);
    font-weight: 400;
    font-size: 30px;
    letter-spacing: 3px;
    line-height: 1.2;
    text-transform: uppercase;
  }
  .botanical-art {
    position: absolute;
    left: 250px;
    top: 0;
    width: 380px;
    height: 600px;
    background: radial-gradient(ellipse at 55% 40%, rgba(95,138,132,0.35) 0%, rgba(95,138,132,0.12) 50%, rgba(45,46,48,0) 75%);
  }
  .product-type {
    position: absolute;
    left: 52px;
    bottom: 50px;
    writing-mode: vertical-rl;
    transform: rotate(180deg);
    color: var(--sage);
    font-weight: 700;
    font-size: 60px;
    letter-spacing: 1px;
    line-height: 1;
  }
  .product-info {
    position: absolute;
    left: 160px;
    right: 0;
    top: 676px;
    text-align: center;
  }
  .product-line {
    color: var(--text-light);
    font-weight: 400;
    font-size: 58px;
    letter-spacing: 1px;
    line-height: 1;
  }
  .product-name {
    margin-top: 28px;
    color: var(--text-light);
    font-weight: 700;
    font-size: 86px;
    line-height: 1;
  }
  .product-size {
    margin-top: 32px;
    color: var(--text-muted);
    font-weight: 400;
    font-size: 26px;
    letter-spacing: 0.5px;
  }
</style>
</head>
<body>
  <main class="canvas">
    <section class="label">
      <div class="botanical-art" role="img" aria-label="Fine line botanical illustration of a leafy branch in muted teal"></div>
      <div class="brand">
        <span class="brand-mark"></span>
        <span class="brand-name">Meadow Hollow<br>Beauty</span>
      </div>
      <div class="product-type">FACIAL SERUM</div>
      <div class="product-info">
        <p class="product-line">SKIN CARE</p>
        <p class="product-name">OIL</p>
        <p class="product-size">30 ML/1 OZ</p>
      </div>
    </section>
  </main>
</body>
</html>
```